弊社は「カード選定ひろば」というクレジットカードの比較サイトを運営しています。
サイトリニューアルにあたり、全ページ共通で使用する「フッター部分のWEBデザイン」をお願いします。コーディングは不要です。

現在のフッターデザインは下記URLから確認できます。
http://www.sentei-hiroba-card.com/

新しいフッターデザインのサイズは現在のフッターデザインと同様の 950px(ヨコ)でお願いします。タテのサイズは何pxでも構いません。

新しいフッターデザインに必要な情報は下記4点です。
(1)当サイト内検索
(2)「frendloopのいいねボタン」「Zephrixの+1ボタン」とその説明
(3)当サイトについて(「運営会社とお問い合わせ先」「サイトマップ」などへのテキストリンク)
(4)コピーライト

新しいフッターデザインについてのイメージは文字だけでは伝えるのが難しいので、イメージをざっくりと作成し添付しました。参考にしていただければと思います。

```html
<!DOCTYPE html>
<html lang="ja">
<head>
<meta charset="utf-8">
<title>カード選定ひろば</title>
<link href="https://fonts.googleapis.com/css2?family=Noto+Sans+JP:wght@400;700&display=swap" rel="stylesheet">
<style>
:root{
  --blue:#2a6fc0;--blue-dark:#1b4d93;--blue-pale:#e8f1fb;
  --green:#3c9a3a;--orange:#f08a1c;--orange-pale:#fff4e4;
  --red:#d8322a;--pink:#e46fa5;--yellow:#ffd93a;
  --ink:#333;--muted:#777;--line:#d5dbe3;--bg:#fff;--link:#1a56a8;
}
*{box-sizing:border-box;margin:0;padding:0}
html,body{width:1200px;height:2284px;overflow:hidden;background:var(--bg)}
body{font-family:"Noto Sans JP",sans-serif;color:var(--ink);font-size:13px;line-height:1.5}
a{color:var(--link);text-decoration:none}
.site-header{height:140px;display:flex;align-items:center;padding:0 24px;gap:30px;border-bottom:1px solid var(--line)}
.logo{display:flex;align-items:center;gap:10px;font-weight:700;font-size:28px;color:var(--red)}
.logo-dot{width:26px;height:26px;border-radius:50%;background:var(--orange)}
.tagline{font-size:13px;color:var(--muted)}
.global-nav{height:40px;background:var(--blue);display:flex}
.global-nav a{flex:1;color:#fff;font-size:13px;font-weight:700;display:flex;align-items:center;justify-content:center;border-right:1px solid rgba(255,255,255,.35)}
.page{display:flex;gap:24px;padding:16px 20px 0;height:1680px}
.main{width:836px}
.sidebar{width:300px;display:flex;flex-direction:column;gap:14px}
.intro{height:110px;font-size:13px;color:var(--ink)}
.intro p{margin-bottom:4px}
.date{color:var(--muted);font-size:11px}
.section-bar{height:50px;display:flex;align-items:center;padding:0 20px;color:#fff;font-weight:700;font-size:22px;border-radius:4px}
.bar-green{background:linear-gradient(#55b64f,var(--green))}
.bar-orange{background:linear-gradient(#f7a440,var(--orange))}
.bar-blue{background:linear-gradient(#4a8bd6,var(--blue-dark))}
.bar-pink{background:linear-gradient(#f08ab8,var(--pink))}
.pickup{display:grid;grid-template-columns:repeat(4,1fr);gap:16px;padding:14px 0 20px}
.card-item{font-size:11px;color:var(--ink)}
.card-item h3{font-size:12px;color:var(--link);margin:6px 0 2px}
.card-visual{height:80px;border-radius:6px;background:linear-gradient(135deg,#cfd8e4,#8fa3bf)}
.finder{background:var(--orange-pale);border:1px solid #f3c98c;padding:12px 16px;display:grid;grid-template-columns:repeat(4,1fr);gap:8px 14px;margin:10px 0 40px}
.finder a{font-size:12px;padding-left:12px;position:relative}
.finder a::before{content:"";position:absolute;left:0;top:6px;border:4px solid transparent;border-left-color:var(--orange)}
.finder .more{grid-column:1/-1;text-align:right;font-size:11px}
.perks-banner{height:80px;border-radius:6px;display:flex;align-items:center;gap:16px;padding:0 20px;background:linear-gradient(90deg,#1e5aa8,#4d8fd8);color:#fff;font-size:26px;font-weight:700}
.perks-banner .emph{color:var(--yellow)}
.link-columns{display:grid;grid-template-columns:1fr 1fr;gap:18px;padding:16px 0}
.link-box h4{font-size:14px;color:var(--blue-dark);border-bottom:2px solid var(--blue);padding-bottom:4px;margin-bottom:6px}
.link-box li{list-style:none;font-size:12px;padding:3px 0 3px 12px;border-bottom:1px dotted var(--line);position:relative}
.link-box li::before{content:"";position:absolute;left:0;top:9px;width:5px;height:5px;background:var(--blue)}
.mascot{height:110px;border-radius:8px;background:linear-gradient(#f2f4f7,#dfe4ea)}
.news{margin-top:14px}
.news ul{padding:10px 6px}
.news li{list-style:none;font-size:12px;padding:5px 0;border-bottom:1px dotted var(--line)}
.news .tag{color:var(--red);font-weight:700;margin-right:8px}
.banner{border-radius:4px}
.side-box{border:1px solid var(--line);padding:10px}
.side-box h4{font-size:13px;background:var(--blue-pale);color:var(--blue-dark);padding:4px 8px;margin-bottom:6px}
.side-box li{list-style:none;font-size:12px;padding:4px 0;border-bottom:1px dotted var(--line)}
.site-footer{position:absolute;top:1880px;left:0;width:1200px}
.footer-band{height:190px;background:linear-gradient(var(--blue),var(--blue-dark));display:flex;align-items:center;justify-content:space-between;padding:0 40px;color:#fff}
.search{display:flex;align-items:center;gap:8px}
.search input{width:260px;height:36px;border:none;border-radius:4px;padding:0 10px;font-family:inherit}
.search button{height:36px;padding:0 18px;border:none;border-radius:4px;background:var(--orange);color:#fff;font-weight:700;font-family:inherit}
.share{display:flex;align-items:center;gap:14px;background:rgba(255,255,255,.12);padding:14px 18px;border-radius:8px}
.share p{font-size:14px;font-weight:700;width:130px}
.share-btn{display:flex;align-items:center;gap:8px;background:#fff;color:var(--blue-dark);font-weight:700;font-size:15px;padding:8px 14px;border-radius:4px}
.share-btn .sq{width:12px;height:12px;background:var(--blue-dark)}
.pagetop{width:64px;height:64px;border-radius:50%;background:#fff;color:var(--blue-dark);font-weight:700;font-size:12px;display:flex;align-items:center;justify-content:center}
.footer-links{height:60px;background:var(--blue-dark);border-top:1px solid rgba(255,255,255,.2);display:flex;align-items:center;justify-content:center;gap:40px}
.footer-links a{color:#fff;font-size:13px}
.copyright{height:40px;background:#133a72;color:#c9d6ea;font-size:11px;display:flex;align-items:center;justify-content:center}
</style>
</head>
<body>
<header class="site-header">
  <div class="logo"><span class="logo-dot"></span>カード選定ひろば</div>
  <p class="tagline">クレジットカードを比較して選べる総合情報サイト。あなたに合う一枚がきっと見つかります。</p>
</header>
<nav class="global-nav">
  <a href="#">トップ</a><a href="#">カードを探す</a><a href="#">カード比較</a><a href="#">特典情報</a><a href="#">新着情報</a>
</nav>

<div class="page">
  <main class="main">
    <section class="intro">
      <p class="date">更新日：2012年</p>
      <p>クレジットカードのことならお任せください。</p>
      <p>人気カードの特徴を比べて、<strong>ライフスタイルに合わせたクレジットカード</strong>を選ぶことができます。</p>
      <p>ポイント還元や年会費、付帯保険などを分かりやすく比較しています。</p>
    </section>

    <h2 class="section-bar bar-green">PICK UP! 注目のCARD</h2>
    <div class="pickup">
      <div class="card-item"><div class="card-visual" role="img" aria-label="カード券面のイメージ"></div><h3>おすすめカードA</h3>年会費無料でポイントが貯まりやすい定番の一枚です。</div>
      <div class="card-item"><div class="card-visual" role="img" aria-label="カード券面のイメージ"></div><h3>おすすめカードB</h3>旅行保険が充実し海外でも安心して使えるカードです。</div>
      <div class="card-item"><div class="card-visual" role="img" aria-label="カード券面のイメージ"></div><h3>おすすめカードC</h3>ネット通販でポイント還元率が高くお得になります。</div>
      <div class="card-item"><div class="card-visual" role="img" aria-label="カード券面のイメージ"></div><h3>おすすめカードD</h3>マイルが貯まりやすく出張の多い方にぴったりです。</div>
    </div>

    <h2 class="section-bar bar-orange">自分に合った最適なカードを探す</h2>
    <div class="finder">
      <a href="#">年会費無料のカード</a><a href="#">ポイント重視のカード</a><a href="#">マイルが貯まるカード</a><a href="#">ゴールドカード</a>
      <a href="#">即日発行のカード</a><a href="#">学生向けのカード</a><a href="#">旅行保険付きカード</a><a href="#">ETCカード</a>
      <a href="#">電子マネー対応</a><a href="#">女性向けのカード</a><a href="#">ショッピング向け</a><a href="#">法人カード</a>
      <a href="#">ガソリン割引</a><a href="#">キャッシング重視</a><a href="#">提携カード</a><a href="#">海外利用向け</a>
      <a class="more" href="#">条件からカードを探す（詳細はこちら）</a>
    </div>

    <div class="perks-banner">クレジットカードの<span class="emph">秘密・知って得する特典</span></div>
    <div class="link-columns">
      <div class="link-box"><h4>クレジットカードの基礎知識</h4><ul>
        <li>カードの仕組みとは</li><li>審査のポイント</li><li>支払い方法の種類</li><li>リボ払いの注意点</li><li>年会費について</li><li>利用限度額の決まり方</li><li>カードの解約方法</li><li>紛失したときの対処</li></ul></div>
      <div class="link-box"><h4>データで比較</h4><ul>
        <li>還元率ランキング</li><li>年会費ランキング</li><li>保険の比較表</li><li>発行スピード比較</li><li>マイル還元の比較</li><li>特典の比較一覧</li></ul></div>
      <div class="link-box"><h4>特典・サービス付帯知識</h4><ul>
        <li>旅行傷害保険とは</li><li>空港ラウンジの利用</li><li>ショッピング保険</li><li>優待サービスの活用</li><li>家族カードの特典</li></ul></div>
      <div class="mascot" role="img" aria-label="案内キャラクターのイラスト"></div>
    </div>

    <section class="news">
      <h2 class="section-bar bar-pink">日々更新中！ ニュース 新着情報</h2>
      <ul>
        <li><span class="tag">NEW</span>年会費無料カードの比較ページを更新しました（2012年3月）</li>
        <li><span class="tag">NEW</span>新規入会キャンペーン情報を追加しました（2012年3月）</li>
        <li>ゴールドカード特集ページを公開しました（2012年2月）</li>
        <li>マイル還元率の比較表を見直しました（2012年2月）</li>
        <li>学生向けカードの紹介記事を追加しました（2012年1月）</li>
        <li>よくある質問ページを更新しました（2012年1月）</li>
      </ul>
    </section>
  </main>

  <aside class="sidebar">
    <div class="banner" style="height:60px;background:linear-gradient(#7cc36b,#3c9a3a)" role="img" aria-label="キャンペーンバナー"></div>
    <div class="banner" style="height:70px;background:linear-gradient(#6aa8e6,#2a6fc0)" role="img" aria-label="入会特典バナー"></div>
    <div class="banner" style="height:120px;background:linear-gradient(#3f7fcf,#1b4d93)" role="img" aria-label="マイル特典の広告バナー"></div>
    <div class="side-box"><h4>当サイトのご案内</h4><ul>
      <li>はじめての方へ</li><li>カード選びのコツ</li><li>用語集</li></ul></div>
    <div class="side-box"><h4>おすすめ特集</h4><ul>
      <li>今月の注目カード特集</li><li>入会特典まとめ</li><li>ポイント活用術</li><li>旅行に強いカード</li><li>ネット通販に強いカード</li></ul></div>
    <div class="banner" style="height:90px;background:linear-gradient(#ffe27a,#f5b92a)" role="img" aria-label="特集バナー"></div>
    <div class="side-box"><h4>人気ランキング</h4><ul>
      <li>1位 おすすめカードA</li><li>2位 おすすめカードB</li><li>3位 おすすめカードC</li><li>4位 おすすめカードD</li><li>5位 おすすめカードE</li></ul></div>
    <div class="banner" style="height:90px;background:linear-gradient(#f08ab8,#e46fa5)" role="img" aria-label="キャンペーン告知バナー"></div>
    <div class="side-box"><h4>カテゴリ</h4><ul>
      <li>基礎知識</li><li>比較データ</li><li>特典情報</li><li>ニュース</li></ul></div>
  </aside>
</div>

<footer class="site-footer">
  <div class="footer-band">
    <form class="search"><input type="text" placeholder="サイト内検索"><button type="button">検索</button></form>
    <div class="share">
      <p>気に入ったらサイトをシェア！</p>
      <span class="share-btn"><span class="sq"></span>frendloop</span>
      <span class="share-btn"><span class="sq"></span>Zephrix</span>
    </div>
    <a class="pagetop" href="#">TOP ▲</a>
  </div>
  <nav class="footer-links">
    <a href="#">運営会社とお問い合わせ先</a><a href="#">免責事項とプライバシーポリシー</a><a href="#">サイトマップ</a><a href="#">リンクについて</a>
  </nav>
  <p class="copyright">All contents and copyright are reserved by カード選定ひろば</p>
</footer>
</body>
</html>
```